Design our branded business card!

We'd love for you to design our business card and come up with a fitting design that reflects the Brimble brand. We're a growing tech startup with big ambitions. We've included our brand guidelines (contain colour palette), logo (EPS vector in CMYK) and old designs to help you on your way.

We'd like to keep the design fairly simple:

* Name
* Phone number
* Email address
* Website (www.brimble.life)
* Twitter (@brimble)
* Address (19 Fenwick Row, Leeds, UK, LS4 9QT).

This would need to include print and cutting marks.

If you have any questions just let us know!

Target Market(s)

Businesses, Press and our customers!

Industry/Entity Type

Business

Contact Information for Business Card

* Name
* Phone number
* Email address
* Twitter (@brimble)

Font styles to use
Sans Serif

Requirements
Must have
• 1. Must have the Brimble logo included.
• 2. Must use the font 'Brandon Text' in either 'light' or 'thin' (https://www.typevaultex.com/fonts/qrnfoundry/brandon-text/)
• 3. Must use exact colours references from the brand guidelines. Colours outside of the brand guidelines will be discounted. White (transparent) backgrounds are fine.
• 4. Must contain the following information:
• * Name
• * Phone number
• * Email address
• * Website (www.brimble.life)
• * Twitter (@brimble)
• * Address (19 Fenwick Row, Leeds, UK, LS4 9QT).
Nice to have
• Must use the font 'Brandon Text' in either 'light' or 'thin' (https://www.typevaultex.com/fonts/qrnfoundry/brandon-text/)
Should not have
• Colours outside of the brand guidelines will be discounted. White (transparent) backgrounds are fine.
• Avoid creating icons or including photography.

```html
<!DOCTYPE html>
<html lang="en">
<head>
<meta charset="utf-8">
<title>Brimble business card</title>
<link rel="stylesheet" href="https://fonts.googleapis.com/css2?family=Nunito+Sans:wght@300;400&display=swap">
<style>
  :root {
    --bg: #ececec;
    --paper: #f5f5f3;
    --charcoal: #4a4f50;
    --green: #7dbb6f;
    --white: #ffffff;
  }
  * { margin: 0; padding: 0; box-sizing: border-box; }
  html, body { width: 1200px; height: 857px; overflow: hidden; }
  body {
    background: var(--bg);
    font-family: "Nunito Sans", sans-serif;
    font-weight: 300;
    position: relative;
  }
  .card {
    position: absolute;
    width: 540px;
    height: 310px;
    overflow: hidden;
    box-shadow: 0 4px 14px rgba(0,0,0,0.12);
  }
  .card-front { left: 40px; top: 330px; background: var(--paper); }
  .card-back { left: 620px; top: 217px; background: var(--charcoal); }

  .front-art { position: absolute; inset: 0; }

  .brand { position: absolute; display: flex; align-items: center; gap: 14px; }
  .brand-dot { width: 60px; height: 60px; border-radius: 50%; background: var(--green); flex: none; }
  .brand-name { font-size: 50px; font-weight: 300; letter-spacing: 1px; line-height: 1; }
  .card-front .brand { left: 34px; top: 100px; }
  .card-front .brand-name { color: var(--charcoal); }
  .card-back .brand { left: 50%; top: 50%; transform: translate(-50%, -50%); }
  .card-back .brand-dot { width: 68px; height: 68px; }
  .card-back .brand-name { color: var(--white); font-size: 56px; }

  .contact-list { position: absolute; list-style: none; color: var(--charcoal); font-size: 13px; line-height: 1.35; }
  .contact-list li { display: flex; align-items: flex-start; gap: 8px; margin-bottom: 2px; }
  .contact-list svg { width: 12px; height: 12px; flex: none; margin-top: 3px; }
  .contact-personal { left: 36px; top: 192px; }
  .contact-company { left: 190px; top: 246px; }

  .person { position: absolute; right: 20px; top: 186px; text-align: right; }
  .person-name { color: var(--green); font-size: 18px; letter-spacing: 1.5px; font-weight: 400; line-height: 1.2; }
  .person-title { color: var(--white); font-size: 12px; margin-top: 3px; }
</style>
</head>
<body>

<section class="card card-front">
  <svg class="front-art" viewBox="0 0 540 310" width="540" height="310">
    <path d="M0 0 H540 V310 H450 C400 280 368 220 355 170 C330 90 220 40 0 30 Z" fill="var(--charcoal)"/>
    <path d="M0 30 C220 40 330 90 355 170 C368 220 400 280 450 310" fill="none" stroke="var(--green)" stroke-width="5"/>
    <path d="M0 22 C180 30 270 48 330 80" fill="none" stroke="var(--green)" stroke-width="9"/>
    <path d="M20 42 C225 52 325 100 348 178 C360 225 390 282 438 310" fill="none" stroke="var(--green)" stroke-width="2"/>
  </svg>

  <div class="brand">
    <span class="brand-dot"></span>
    <span class="brand-name">brimble</span>
  </div>

  <ul class="contact-list contact-personal">
    <li>
      <svg viewBox="0 0 13 13"><rect x="3" y="0.5" width="7" height="12" rx="1.2" fill="none" stroke="var(--green)"/><line x1="5.5" y1="10.5" x2="7.5" y2="10.5" stroke="var(--green)"/></svg>
      +44 (0) 000 000 00
    </li>
    <li>
      <svg viewBox="0 0 13 13"><rect x="0.5" y="2.5" width="12" height="8" fill="var(--green)"/><path d="M0.5 2.5 L6.5 7 L12.5 2.5" fill="none" stroke="var(--paper)"/></svg>
      yourname@brimble.life
    </li>
    <li>
      <svg viewBox="0 0 13 13"><circle cx="6.5" cy="6.5" r="5.5" fill="var(--green)"/></svg>
      @brimble
    </li>
  </ul>

  <ul class="contact-list contact-company">
    <li>
      <svg viewBox="0 0 13 13"><circle cx="6.5" cy="6.5" r="5.5" fill="none" stroke="var(--green)"/><ellipse cx="6.5" cy="6.5" rx="2.3" ry="5.5" fill="none" stroke="var(--green)"/><line x1="1" y1="6.5" x2="12" y2="6.5" stroke="var(--green)"/></svg>
      www.brimble.life
    </li>
    <li>
      <svg viewBox="0 0 13 13"><path d="M6.5 12.5 C3 8 2 6.5 2 5 A4.5 4.5 0 0 1 11 5 C11 6.5 10 8 6.5 12.5 Z" fill="var(--green)"/><circle cx="6.5" cy="5" r="1.6" fill="var(--paper)"/></svg>
      19 Fenwick Row, Leeds,<br>UK LS4 9QT
    </li>
  </ul>

  <div class="person">
    <p class="person-name">YOUR NAME</p>
    <p class="person-title">Your Title</p>
  </div>
</section>

<section class="card card-back">
  <div class="brand">
    <span class="brand-dot"></span>
    <span class="brand-name">brimble</span>
  </div>
</section>

</body>
</html>
```